Vending machine glass sticker

We need a few stickers designed to promote our new electronics products. The primary sticker will be placed along the bottom of the glass of our vending machines, and the secondary sticker will be placed up each of the sides inside the machine cabinet. We want to use eye-catching bright colours, so long as they don't clash with our machines and products. See attached Powerpoint file for examples. Slide 4 also has product images and logos you can use.DimensionsPrimary sticker: 850mm (w) x ~100mm (h) - the height is flexible, and doesn't need to be uniform across the design (i.e. slope is OK)Secondary sticker: 130mm (w) x 1100mm (h)

```html
<!DOCTYPE html>
<html lang="en">
<head>
<meta charset="utf-8">
<title>Cabinet side stickers – colour options</title>
<link href="https://fonts.googleapis.com/css2?family=Barlow+Condensed:ital,wght@1,600;1,800&family=Comfortaa:wght@400&display=swap" rel="stylesheet">
<style>
  :root{
    --canvas:#000;
    --teal-bg:#0b363d; --teal-ink:#2bea6b;
    --violet-bg:#5410b8; --violet-ink:#1de0ef;
    --red-bg:#f0201f; --red-ink:#ffe600;
    --logo-ink:#ffffff;
  }
  html,body{margin:0;padding:0;overflow:hidden;background:var(--canvas);}
  .canvas{position:relative;width:1187px;height:1200px;background:var(--canvas);overflow:hidden;}
  .sticker{position:absolute;top:55px;width:129px;height:1088px;overflow:hidden;
    background:var(--bg);color:var(--ink);font-family:"Barlow Condensed",sans-serif;font-style:italic;}
  .sticker--teal{left:237px;--bg:var(--teal-bg);--ink:var(--teal-ink);}
  .sticker--violet{left:528px;--bg:var(--violet-bg);--ink:var(--violet-ink);}
  .sticker--red{left:812px;--bg:var(--red-bg);--ink:var(--red-ink);}

  .headline{position:absolute;left:6px;width:118px;top:30px;text-align:center;font-weight:800;margin:0;}
  .headline span{display:block;white-space:nowrap;}
  .headline .lead{font-size:23px;line-height:24px;}
  .headline .big{font-size:56px;line-height:48px;letter-spacing:-1px;}
  .headline .mid{font-size:18px;line-height:18px;}
  .headline .time{font-size:48px;line-height:44px;letter-spacing:-1px;margin-top:2px;}
  .headline .end{font-size:31px;line-height:32px;}

  .product{position:absolute;}
  .product--powerbank{left:13px;top:253px;width:130px;height:127px;border-radius:8px;
    transform:skewY(28deg);transform-origin:top left;top:253px;height:68px;
    background:linear-gradient(135deg,#d9d9dc,#9a9aa0 60%,#6d6d72);}
  .product--charger{left:16px;top:514px;width:89px;height:85px;border-radius:10px;
    background:linear-gradient(150deg,#ffffff,#d8d8d8 70%,#b9b9b9);}
  .product--cable{left:0;top:759px;width:105px;height:174px;
    background:linear-gradient(125deg,transparent 40%,rgba(255,255,255,.85) 41%,rgba(255,255,255,.85) 47%,transparent 48%,transparent 58%,rgba(255,255,255,.9) 59%,rgba(255,255,255,.9) 66%,transparent 67%);}

  .needs{position:absolute;left:9px;width:118px;margin:0;font-weight:600;}
  .needs h2{margin:0 0 6px;font-size:12px;line-height:14px;font-weight:800;}
  .needs ul{list-style:none;margin:0;padding:0;font-size:8px;line-height:13px;}
  .needs li::before{content:"• ";}
  .needs--top{top:412px;}
  .needs--bottom{top:637px;}

  .disclaimer{position:absolute;right:12px;top:959px;width:118px;margin:0;text-align:right;
    font-size:8px;line-height:13px;font-weight:800;}

  .brand{position:absolute;left:0;width:129px;top:1042px;text-align:center;
    font-family:"Comfortaa",sans-serif;font-style:normal;font-size:20px;color:var(--logo-ink);letter-spacing:.5px;}
</style>
</head>
<body>
<div class="canvas">

  <section class="sticker sticker--teal">
    <h1 class="headline"><span class="lead">Refill Up To</span><span class="big">50%</span><span class="mid">Of Your Phone's</span><span class="mid">Battery in Just</span><span class="time">00:30</span><span class="end">Minutes!</span></h1>
    <div class="product product--powerbank" role="img" aria-label="Slim silver power bank"></div>
    <div class="needs needs--top"><h2>What you need:</h2><ul><li>mPhone 8 and up</li><li>Cert USB-C to Bolt cable</li><li>30W USB-C Wall Charger</li></ul></div>
    <div class="product product--charger" role="img" aria-label="White dual-port wall charger"></div>
    <div class="needs needs--bottom"><ul><li>Flux 10 Plus or Flux 20 Max power bank Other devices with USB-C charge ports</li><li>30W USB-C Wall Charger</li><li>Flux 10 Plus or Flux 20 Max Power Bank</li></ul></div>
    <div class="product product--cable" role="img" aria-label="White charging cable"></div>
    <p class="disclaimer">For compatible devices.<br>Charge speeds vary by model.<br>Check your device's user<br>manual for more info.</p>
    <div class="brand">chargebay</div>
  </section>

  <section class="sticker sticker--violet">
    <h1 class="headline"><span class="lead">Refill Up To</span><span class="big">50%</span><span class="mid">Of Your Phone's</span><span class="mid">Battery in Just</span><span class="time">00:30</span><span class="end">Minutes!</span></h1>
    <div class="product product--powerbank" role="img" aria-label="Slim silver power bank"></div>
    <div class="needs needs--top"><h2>What you need:</h2><ul><li>mPhone 8 and up</li><li>Cert USB-C to Bolt cable</li><li>30W USB-C Wall Charger</li></ul></div>
    <div class="product product--charger" role="img" aria-label="White dual-port wall charger"></div>
    <div class="needs needs--bottom"><ul><li>Flux 10 Plus or Flux 20 Max power bank Other devices with USB-C charge ports</li><li>30W USB-C Wall Charger</li><li>Flux 10 Plus or Flux 20 Max Power Bank</li></ul></div>
    <div class="product product--cable" role="img" aria-label="White charging cable"></div>
    <p class="disclaimer">For compatible devices.<br>Charge speeds vary by model.<br>Check your device's user<br>manual for more info.</p>
    <div class="brand">chargebay</div>
  </section>

  <section class="sticker sticker--red">
    <h1 class="headline"><span class="lead">Refill Up To</span><span class="big">50%</span><span class="mid">Of Your Phone's</span><span class="mid">Battery in Just</span><span class="time">00:30</span><span class="end">Minutes!</span></h1>
    <div class="product product--powerbank" role="img" aria-label="Slim silver power bank"></div>
    <div class="needs needs--top"><h2>What you need:</h2><ul><li>mPhone 8 and up</li><li>Cert USB-C to Bolt cable</li><li>30W USB-C Wall Charger</li></ul></div>
    <div class="product product--charger" role="img" aria-label="White dual-port wall charger"></div>
    <div class="needs needs--bottom"><ul><li>Flux 10 Plus or Flux 20 Max power bank Other devices with USB-C charge ports</li><li>30W USB-C Wall Charger</li><li>Flux 10 Plus or Flux 20 Max Power Bank</li></ul></div>
    <div class="product product--cable" role="img" aria-label="White charging cable"></div>
    <p class="disclaimer">For compatible devices.<br>Charge speeds vary by model.<br>Check your device's user<br>manual for more info.</p>
    <div class="brand">chargebay</div>
  </section>

</div>
</body>
</html>
```